Waste Oil Filter collection & disposal

Basically I need a 1 page website for the business called Brenmoor Waste Solutions.
We are a environmental service provider and we collect and dispose of waste oil filters to protect the environment from hazardous waste oil products.

This is the link to our current website: www.brenmoorwaste.co.nz

we want it to look fresh and better than our current website. we may potentially look at getting a new logo designed and are open to ideas/designs if you have any.

Industry/Entity Type

Business

Logo Text

Brenmoor Waste Solutions

Number of Pages Required

1 page

Requirements
Must have
• same colours as current website.
• description of what service we provide please refer to leaflet attached

```html
<!DOCTYPE html>
<html lang="en">
<head>
<meta charset="utf-8">
<title>Brenmoor Waste Solutions</title>
<link href="https://fonts.googleapis.com/css2?family=Roboto+Condensed:wght@300;400&display=swap" rel="stylesheet">
<style>
:root{
  --green:#2a8c6e;
  --navy:#2f3e6b;
  --ink:#333;
  --muted:#7a7a7a;
  --hero:#d3d3d3;
  --band:#ededed;
  --field:#e6e7e9;
  --link:#2e4ea0;
  --white:#fff;
}
*{box-sizing:border-box;margin:0;padding:0}
html,body{width:961px;height:1200px;overflow:hidden;background:var(--white)}
body{font-family:"Roboto Condensed",sans-serif;font-weight:300;color:var(--ink);position:relative}
.abs{position:absolute}

/* header */
.brand-mark{left:64px;top:17px;width:84px;height:84px;border-radius:50%;background:var(--green)}
.brand-name{left:160px;top:26px;font-size:23px;line-height:26px;color:var(--muted);letter-spacing:.3px}
.brand-tag{left:160px;top:82px;font-size:11.5px;color:var(--muted);font-weight:400;letter-spacing:.3px}
.contact-item{top:51px;display:flex;align-items:center;gap:7px;font-size:14.5px;font-weight:400;color:var(--ink)}
.contact-item svg{width:16px;height:16px}

/* hero */
.hero{left:0;top:120px;width:961px;height:302px;background:var(--hero)}
.hero-photo{left:56px;top:16px;width:444px;height:272px;border-radius:4px;background:linear-gradient(135deg,#bfc3c2 0%,#a9aeac 45%,#2f8f6f 75%,#7f8684 100%)}
.hero-copy{left:552px;top:30px;width:350px;text-align:center}
.hero-copy h1{font-weight:300;font-size:27px;line-height:32px;color:var(--navy);letter-spacing:.3px}
.hero-copy p{font-size:14.5px;line-height:19px;margin-top:15px;color:#3c3c3c}
.hero-copy h1+p{margin-top:26px}

/* pricing */
.price{top:440px;width:260px;text-align:center}
.price svg{height:100px;display:block;margin:0 auto}
.price span{display:block;margin-top:18px;font-size:20px;color:#2a2a2a}

/* process band */
.band{left:0;top:606px;width:961px;height:298px;background:var(--band)}
.process{left:61px;top:22px;width:230px}
.process h2,.oil h2{font-weight:300;font-size:21px;color:#222}
.process p{font-size:13.5px;line-height:17.5px;margin:8px 0 0 7px;color:#333}
.process ul{list-style:none;margin-top:6px}
.process li{font-size:13.5px;line-height:26.4px;color:#333}
.process li::before{content:"· "}
.process-photo{left:301px;top:10px;width:347px;height:277px;border:2px solid #b7b7b7;background:linear-gradient(160deg,#8b8f8c 0%,#4c514f 40%,#2a8073 62%,#bdbdbd 100%)}
.oil{left:675px;top:14px;width:265px}
.oil > p{font-size:12px;line-height:16px;margin:6px 0 0 6px;color:#333}
.oil > p + p{margin-top:8px}
.quote{border-top:1px solid #d8d8d8;margin-top:8px;padding:6px 6px 0;font-size:8.6px;line-height:12.5px;color:#333;font-weight:400}
.quote .src{color:var(--link);font-size:9px}

/* lower */
.map{left:69px;top:920px;width:181px;height:168px;border:2px solid #b9b9b9;background:linear-gradient(155deg,#f1f1f1 0%,#ececec 55%,#b9d3ef 72%,#eaeaea 86%)}
.directions{left:69px;top:1100px;width:180px;height:23px;background:var(--green);color:var(--white);font-size:16px;font-weight:400;display:flex;align-items:center;justify-content:center;gap:8px;letter-spacing:.3px}
.hours{left:79px;top:1134px;display:flex;gap:14px;font-size:11.5px;line-height:16px;font-weight:400;color:#333}
.hours .label{width:50px}
.hours .rule{width:1px;height:30px;background:#333;margin-top:1px}
.pitch{left:318px;top:920px;width:340px;text-align:center;font-size:18.5px;line-height:25px;color:#444}
.pitch p{margin-bottom:16px}
.pitch p:last-child{margin-top:10px}
.contact{left:699px;top:922px;width:200px}
.contact h2{font-weight:300;font-size:20px;color:#222}
.field-label{font-size:9px;font-weight:400;margin:13px 0 4px 10px;color:#333}
.field{margin-left:9px;width:183px;height:19px;background:var(--field);border:1px solid #cfd0d2}
.field.tall{height:64px}
.send{left:843px;top:1134px;width:48px;height:24px;background:#ececec;border:1px solid #cfcfcf;font-size:15px;font-weight:400;display:flex;align-items:center;justify-content:center;color:#333}

.footer{left:0;top:1174px;width:961px;height:26px;background:var(--navy);color:var(--white);font-size:10.5px;font-weight:400;text-align:center;line-height:26px}
</style>
</head>
<body>

<header>
  <div class="abs brand-mark"></div>
  <div class="abs brand-name">BRENMOOR WASTE<br>SOLUTIONS LTD</div>
  <div class="abs brand-tag">Our aim is to keep NZ Green</div>

  <div class="abs contact-item" style="left:382px">
    <svg viewBox="0 0 16 16" fill="none" stroke="#333" stroke-width="1.2"><circle cx="8" cy="8" r="7"/><ellipse cx="8" cy="8" rx="3" ry="7"/><path d="M1 8h14M2.5 4.5h11M2.5 11.5h11"/></svg>
    www.brenmoorwaste.co.nz
  </div>
  <div class="abs contact-item" style="left:580px">
    <svg viewBox="0 0 16 16"><path d="M1 4h14v9H1z" fill="#333"/><path d="M1 4l7 5 7-5" fill="none" stroke="#fff" stroke-width="1.2"/></svg>
    info@brenmoorwaste.co.nz
  </div>
  <div class="abs contact-item" style="left:795px;gap:12px">
    <svg viewBox="0 0 16 16"><path d="M3 1.5l3 .5 1 3.5-1.8 1.2a8 8 0 0 0 4 4L10.5 9l3.5 1 .5 3c-1 1.5-3 1.8-5 1A13 13 0 0 1 2 6C1.2 4 1.5 2.5 3 1.5z" fill="#333"/></svg>
    06 555 0142
  </div>
</header>

<section class="abs hero">
  <div class="abs hero-photo" role="img" aria-label="Green and grey filter collection truck"></div>
  <div class="abs hero-copy">
    <h1>BRENMOOR WASTE SOLUTIONS<br>KEEPING NEW ZEALAND GREEN</h1>
    <p>Brenmoor Waste Solutions Ltd specialize in the collection &amp; disposal of oil / fuel filters, servicing the lower north island on a monthly cycle.</p>
    <p>We offer a cost effective environmentally friendly system for the collection and disposal of waste oil filters helping minimise contamination of landfills keeping your industry compliant.</p>
  </div>
</section>

<section class="pricing">
  <div class="abs price" style="left:65px">
    <svg viewBox="0 0 100 100" width="100"><path d="M42 22L64 2h20v70H42z" fill="#222"/><rect x="6" y="24" width="24" height="5" rx="1.5" fill="#222"/><path d="M8 31h20l-2 38H10z" fill="#222"/><circle cx="52" cy="82" r="13" fill="#222"/><circle cx="52" cy="82" r="7" fill="#fff"/></svg>
    <span>Monthly Bin Collection: $65.00</span>
  </div>
  <div class="abs price" style="left:360px">
    <svg viewBox="0 0 140 100" width="140"><g fill="#222"><rect x="2" y="6" width="40" height="7" rx="2"/><path d="M5 15h34l-3 70H8z"/><rect x="6" y="82" width="10" height="10" rx="5"/><rect x="28" y="82" width="10" height="10" rx="5"/><rect x="50" y="6" width="40" height="7" rx="2"/><path d="M53 15h34l-3 70H56z"/><rect x="54" y="82" width="10" height="10" rx="5"/><rect x="76" y="82" width="10" height="10" rx="5"/><rect x="98" y="6" width="40" height="7" rx="2"/><path d="M101 15h34l-3 70h-28z"/><rect x="102" y="82" width="10" height="10" rx="5"/><rect x="124" y="82" width="10" height="10" rx="5"/></g></svg>
    <span>Additional Bins: $35.00 ea</span>
  </div>
  <div class="abs price" style="left:645px">
    <svg viewBox="0 0 100 100" width="100" fill="none" stroke="#222" stroke-width="2"><circle cx="50" cy="50" r="39"/><circle cx="50" cy="38" r="12"/><path d="M32 63c0-10 8-14 18-14s18 4 18 14z"/><path d="M35 69h30M40 74h20"/><circle cx="73" cy="73" r="13" fill="#fff"/><path d="M73 66v14M66 73h14"/></svg>
    <span>Accaunt Set Up Fee: $85.00</span>
  </div>
</section>

<section class="abs band">
  <div class="abs process">
    <h2>The Process</h2>
    <p>Filters are collected and transported back to the processing plant.<br>At the processing plant they are:</p>
    <ul>
      <li>Drained</li>
      <li>Sorted</li>
      <li>Drained again</li>
      <li>Crushed into bricks</li>
      <li>Drained a third time</li>
      <li>Stacked ready for Metal Recycling</li>
    </ul>
  </div>
  <div class="abs process-photo" role="img" aria-label="Oil filters on the processing plant conveyor"></div>
  <div class="abs oil">
    <h2>What Happens to the Oil</h2>
    <p>All residual oil is collected into our<br>tank and then recycled.</p>
    <p>Currently we are processing over 2,000<br>litres of oil a month.</p>
    <div class="quote">"Recycling engine oil protects the environment and conserves energy resources"<br><span class="src">-Oil Recyciling</span></div>
    <div class="quote">"One litre of used oil can contaminate one million litres of water"<br><span class="src">-Harbourview City<br>Council</span></div>
    <div class="quote">"Each used oil filter has on average, more than quarter of a litre of used motor oil"<br><span class="src">-Westvale Recycle</span></div>
  </div>
</section>

<section class="lower">
  <div class="abs map" role="img" aria-label="Street map of the business location"></div>
  <div class="abs directions">GET DIRECTIONS
    <svg width="13" height="13" viewBox="0 0 14 14" fill="none" stroke="#fff" stroke-width="1.2"><circle cx="7" cy="7" r="6"/><path d="M7 10.5L4.8 7a2.3 2.3 0 1 1 4.4 0z" fill="#fff"/></svg>
  </div>
  <div class="abs hours">
    <div class="label">OPENING<br>HOURS</div>
    <div class="rule"></div>
    <div>Monday - Friday<br>7.30am - 5.00pm</div>
  </div>

  <div class="abs pitch">
    <p>We are passionate about doing our bit<br>in keeping New Zealand Clean and Green.</p>
    <p>We offer a cost effective system for the<br>collection and disposal of waste oil filters.</p>
    <p>Our processes are environmentally friendly<br>and minimise the contamination of landfills.</p>
    <p>We keep our industry compliant.</p>
  </div>

  <form class="abs contact">
    <h2>Contact Us</h2>
    <div class="field-label">Email</div>
    <div class="field"></div>
    <div class="field-label" style="margin-top:15px">Name</div>
    <div class="field"></div>
    <div class="field-label" style="margin-top:13px">Message</div>
    <div class="field tall"></div>
  </form>
  <div class="abs send">SEND</div>
</section>

<footer class="abs footer">Copyright © 2017 Brenmoor Waste Solutions LTD. All Rights Reserved.</footer>

</body>
</html>
```